Activity List

We need a brochure designed for the Brackley House, which is a holiday villa in Sri Lanka. The brochure will be sent to travel agents and holiday travellers by email and also be printed and placed at the Brackley House. The brochure should be sophisticated yet indicate a sense of adventure.

```html
<!DOCTYPE html>
<html lang="en">
<head>
<meta charset="utf-8">
<title>Brackley House – Activity List Brochure</title>
<link rel="stylesheet" href="https://fonts.googleapis.com/css2?family=Questrial&family=Mulish:wght@400;700;800&display=swap">
<style>
  :root{
    --stage:#5e5f61;
    --paper:#ffffff;
    --teal:#2aa59c;
    --green:#2f9a3c;
    --rule:#37a9a0;
    --ink:#3d3d3d;
    --muted:#666;
    --sky-top:#2f6fb6;
    --sky-mid:#8fb8de;
    --hill:#4d6e3c;
  }
  *{box-sizing:border-box;margin:0;padding:0}
  html,body{width:1200px;height:1000px;overflow:hidden}
  body{background:var(--stage);font-family:"Mulish",sans-serif;color:var(--ink);position:relative}
  .spread{position:absolute;left:45px;width:1110px;height:465px;display:flex;box-shadow:0 10px 30px rgba(0,0,0,.35)}
  .spread--outside{top:22px}
  .spread--inside{top:510px}
  .panel{width:370px;height:465px;background:var(--paper);position:relative;overflow:hidden;padding:14px 18px}
  .panel + .panel{border-left:1px solid #e2e2e2}
  .photo{border-radius:10px;width:100%}
  .heading{font-family:"Mulish",sans-serif;font-weight:800;color:var(--green);font-size:11.5px;padding-bottom:3px;border-bottom:1px solid var(--rule);margin:8px 0 5px}
  .heading--large{font-size:13px}
  .section-title{font-family:"Questrial",sans-serif;color:var(--teal);font-size:15px;margin:10px 0 4px}
  p{font-size:8.6px;line-height:1.38;text-align:justify;margin-bottom:4px}
  .price{font-size:8.6px;margin-bottom:4px}

  /* outside: activities panel */
  .activities .photo--canopy{height:105px;border-radius:0;margin:-14px -18px 0;width:calc(100% + 36px);background:linear-gradient(180deg,#1f3b22,#3f6b35 60%,#6c8f4b);position:relative}
  .activities .intro{position:absolute;top:16px;left:120px;right:14px;color:#e8f2e4;font-size:7.5px;text-align:left}
  .photo--pepper{height:110px;background:radial-gradient(circle at 45% 55%,#2f5a1f,#6fa43c 55%,#c9dca1)}

  /* outside: back panel */
  .back{padding:0;background:linear-gradient(180deg,#c9dbed 0%,#eef3f7 30%,#ffffff 55%)}
  .brand{display:flex;flex-direction:column;align-items:center;gap:6px;color:var(--teal);font-family:"Questrial",sans-serif;font-size:15px;letter-spacing:1px}
  .brand__dot{width:26px;height:26px;border-radius:50%;background:var(--teal)}
  .back .brand{margin-top:70px}
  .photo--sign{width:250px;height:120px;margin:26px auto 0;background:linear-gradient(160deg,#8c8c86,#55594f 55%,#7d9a5c)}
  .contact{margin:28px 30px 0;font-family:"Questrial",sans-serif;font-size:11px;line-height:1.6;text-align:right;color:var(--muted)}
  .web{position:absolute;bottom:14px;left:24px;font-family:"Questrial",sans-serif;font-size:10px;color:#fff}

  /* outside: cover */
  .cover{padding:0}
  .photo--cover{position:absolute;inset:0;border-radius:0;height:100%;background:linear-gradient(180deg,var(--sky-top) 0%,var(--sky-mid) 30%,#dfe8ee 45%,#9bb0a8 58%,var(--hill) 78%,#2f4a26 100%)}
  .cover__band{position:absolute;top:0;left:0;right:0;height:170px;background:linear-gradient(180deg,rgba(255,255,255,.96),rgba(255,255,255,.7) 70%,rgba(255,255,255,0))}
  .cover .brand{position:absolute;top:40px;left:0;right:0}
  .tagline{position:absolute;top:150px;left:0;right:0;text-align:center;font-family:"Questrial",sans-serif;font-size:21px;line-height:1.25;color:var(--teal)}

  /* inside */
  .photo--spices{height:90px;margin:6px 0;background:linear-gradient(120deg,#7a2e1c,#b56a32 40%,#6f8a3a 70%,#3c5a25)}
  .photo--gardens{height:92px;margin:6px 0;background:linear-gradient(180deg,#cfd8cf,#8ba27e 50%,#3f5b31)}
  .photo--temple{height:105px;margin:6px 0;background:linear-gradient(180deg,#1d2f6e,#3c4f96 45%,#d59a3e 75%,#6b3b1a)}
  .photo--peak{height:110px;margin-bottom:4px;background:linear-gradient(180deg,#0f2a7a,#2a55b8 60%,#1a3470)}
</style>
</head>
<body>

<section class="spread spread--outside" aria-label="Brochure outside">
  <article class="panel activities">
    <div class="photo photo--canopy" role="img" aria-label="Photo of a forest view framed by a wooden veranda">
      <p class="intro">The Brackley House is a gateway to many of the Central Highlands' finest sights, from waterfalls and temples to tea estates, gardens and misty peaks that reward every kind of traveller.</p>
    </div>
    <h2 class="section-title">Activities at the Brackley House</h2>
    <h3 class="heading">Learn About Coffee and Spice</h3>
    <p>Join us for a morning walk through our 10-acre property, where we grow several different spices and delicious coffee. We show you how the plants are cultivated and encourage you to try your hand at picking any spices that are ready for harvesting, and give you a brief history of the ancient spice trade while you are at it. (Activity provided free of charge)</p>
    <div class="photo photo--pepper" role="img" aria-label="Photo of green peppercorns on the vine"></div>
    <h3 class="heading">From Leaf to Cup (20 minute by foot)</h3>
    <p>Walk down to the neighbourhood tea factory for a lesson on how Sri Lanka's most famous export – tea – is processed. Watch how a batch of freshly picked tea leaves is transformed into the familiar brew that is enjoyed by millions around the world. (Activity provided free of charge based on availability)</p>
  </article>

  <article class="panel back">
    <div class="brand"><span class="brand__dot"></span><span>THE BRACKLEY HOUSE</span></div>
    <div class="photo photo--sign" role="img" aria-label="Photo of the house name sign on a stone wall"></div>
    <address class="contact">
      17/4 Hillcrest Road, Ambawela, Sri Lanka.<br>
      Tel: +94 - 81000 - 1234<br>
      Fax: +94 - 60000 - 5678<br>
      Email: information@brackley-house.com
    </address>
    <span class="web">www.brackley-house.com</span>
  </article>

  <article class="panel cover">
    <div class="photo photo--cover" role="img" aria-label="Photo of a traveller resting on a rock above a forested valley under a blue sky"></div>
    <div class="cover__band"></div>
    <div class="brand"><span class="brand__dot"></span><span>THE BRACKLEY HOUSE</span></div>
    <h1 class="tagline">A tranquility that<br>only nature bestows</h1>
  </article>
</section>

<section class="spread spread--inside" aria-label="Brochure inside">
  <article class="panel">
    <h3 class="heading">The Kotmale Dam (15 minutes)</h3>
    <p>The impressive Kotmale Dam built in the 1980s is just a 15-minute drive from the house. The Brackley House manager will accompany you to the dam and give you details on its construction. Take in the majesty of this engineering wonder and if the waters are low, catch a glimpse of ancient temples that were submerged during its construction. If interested we will then take you to visit the Mahaweli Maha Seya, a gigantic stupa built to replace the lost temples.</p>
    <p class="price">($25 for a group up to 4 people using guest's vehicle, $50 per group in Brackley House vehicle)</p>
    <div class="photo photo--spices" role="img" aria-label="Photo of chillies, limes and spices beside a chopping board"></div>
    <h3 class="heading heading--large">Rice &amp; Spice Cookery Demonstration</h3>
    <p>Spend a morning at the Brackley House with our cook Anura who will show you how to put together that lunch time staple of all Sri Lankan homes – the amazing rice and curry. He will give you tips, show you how to use spices, and even walk you through our gardens to collect produce for your meal. You then get to enjoy the meal you cooked and also receive the Brackley House Lunch, a booklet of rice and curry recipes.</p>
    <p class="price">($25 per person)</p>
    <h3 class="heading heading--large">Hill and Village Walk</h3>
    <p>The Brackley House is located right across from a hill, that dominates our views. For those who like to explore on foot you can cross the stream at the bottom of our property and then walk through a shaded, meandering path that takes you past many village homes. For the more adventurous a steep climb will take you up to the top of the hill for fabulous views of the valley below.</p>
  </article>

  <article class="panel">
    <h3 class="heading">Kitulgala (1 hour)</h3>
    <p>For adventure seekers – there's no better spot than Kitulgala. From white water rafting to canyoning, from kayaking to hiking, Kitulgala offers enough for a half-day or full day of activities.</p>
    <h3 class="heading heading--large">Royal Botanical Gardens, Peradeniya (30 minutes)</h3>
    <p>The Brackley House is located right across from a hill, that dominates our views. For those who like to explore on foot you can cross the stream at the bottom of our property and then walk through a shaded, meandering path that takes you past many village homes. For the more adventurous a steep climb will take you up to the top of the hill for fabulous views of the valley below.</p>
    <div class="photo photo--gardens" role="img" aria-label="Photo of a tall palm avenue in the botanical gardens"></div>
    <h3 class="heading heading--large">Kandy (45 minutes)</h3>
    <p>Kandy is famed for the Dalada Maligawa – the ancient royal palace that now houses the sacred tooth relic of the Lord Buddha. The Kandy Perahera is held each year in August, and is a colourful spectacle of adorned elephants, fire dancers and traditional drummers.</p>
    <div class="photo photo--temple" role="img" aria-label="Photo of the illuminated temple in Kandy at dusk"></div>
  </article>

  <article class="panel">
    <div class="photo photo--peak" role="img" aria-label="Photo of a mountain peak silhouetted against a deep blue sky"></div>
    <h3 class="heading heading--large">Adam's Peak (45 minutes)</h3>
    <p>Adam's Peak is a conspicuous, statuesque, triangular shape that announces its presence amidst its less well-proportioned mountain counterparts. The Peak is famous for its giant footprint, which is considered sacred by Buddhists, Hindus, Muslims and Christians alike. Climbing season commences in December and ends in May. The four-hour hike begins in the dead of night, in time to reach the summit to watch the first rays of sunlight pierce through the darkness to cast a perfect shadow of the mountain on the plains below.</p>
    <h3 class="heading heading--large">The Temple Trio (30 minutes)</h3>
    <p>Step off the beaten track to visit three ancient temples built in the 14th century by kings who ruled the Gampola kingdom. The three temples, Embekke, Gadaladeniya and Lankatilleke were regularly visited by both the kings and their wives. The temples are interesting as despite their close proximity they differ considerably in their architecture.</p>
    <h3 class="heading heading--large">Nuwara Eliya (2.5 hours)</h3>
    <p>Nuwara Eliya is fondly known as Little England - for its lovely Scottish style cottages and manicured gardens. For those who like a spot of golf while on holiday, Nuwara Eliya's golf course is considered one of the finest in Asia. The drive up to Nuwara Eliya from the Brackley House is spectacular as you meander past riverine forests, before breaking into the tea country, where hill-upon-hill is blanketed in brilliant green tea bushes.</p>
  </article>
</section>

</body>
</html>
```